Picture Ads

We need some banner ads for our home business opportunity, we are evolving from text to picture ads. I have added some examples of what other distributors are using. We are looking for something really eye catching with some good key words and nice bright colours and to include our photo (attached)
Key words to include:
Booming online business
Personal Development and Leadership Industry
Earn an executive income from home
Simple 3 step system
Make up to $5,000 per sale
Not MLM
The size needs to be: 1000 x 35 pixels
13.9 x 4.75 Inches
35.3 x 11.1 cm
I think different platforms accept different sizes, not too familiar with it yet, any guidance welcome. I've clicked project for 2 days if that is to prioritise the order?
Many thanks,
Maren

Industry/Entity Type

Business

```html
<!DOCTYPE html>
<html lang="en">
<head>
<meta charset="UTF-8">
<title>Booming Online Business Banner</title>
<link rel="stylesheet" href="https://fonts.googleapis.com/css2?family=Oswald:wght@600&family=Kalam:wght@700&family=Montserrat:wght@600&display=swap">
<style>
  :root {
    --navy-deep: #0a1a3d;
    --navy: #12296b;
    --royal: #1c47b0;
    --yellow: #f6f21c;
    --ink: #1d2433;
    --white: #ffffff;
  }
  * { margin: 0; padding: 0; box-sizing: border-box; }
  html, body { width: 1200px; height: 377px; overflow: hidden; background: var(--white); }
  .banner { position: relative; width: 1200px; height: 377px; overflow: hidden; background: var(--white); }
  .backdrop, .photo { position: absolute; left: 0; top: 0; width: 1200px; height: 306px; }
  .headline {
    position: absolute; left: 46px; top: 14px; width: 770px;
    font-family: 'Oswald', 'Arial Narrow', sans-serif; font-weight: 600;
    font-size: 68px; line-height: 1; color: var(--white);
    text-align: center; white-space: nowrap;
    transform: scaleY(1.22); transform-origin: top center;
  }
  .ribbon { position: absolute; left: 46px; top: 112px; width: 770px; height: 48px; }
  .ribbon-text {
    position: absolute; left: 46px; top: 112px; width: 770px; height: 48px;
    font-family: 'Kalam', cursive; font-weight: 700; font-style: italic;
    font-size: 30px; line-height: 52px; color: var(--ink); text-align: center; white-space: nowrap;
  }
  .offer {
    position: absolute; left: 130px; top: 189px; width: 592px;
    font-family: 'Oswald', 'Arial Narrow', sans-serif; font-weight: 600;
    font-size: 49px; line-height: 1; color: var(--yellow);
    text-align: center; white-space: nowrap;
    transform: scaleY(1.25); transform-origin: top center;
  }
  .stars { position: absolute; top: 214px; width: 72px; height: 18px; }
  .stars-left { left: 46px; }
  .stars-right { left: 736px; }
  .benefits {
    position: absolute; left: 0; top: 306px; width: 1200px; height: 71px;
    display: flex; align-items: center; justify-content: center; gap: 28px;
    font-family: 'Montserrat', Arial, sans-serif; font-weight: 600;
    font-size: 30px; color: var(--ink); white-space: nowrap;
  }
  .benefits .dot { width: 12px; height: 12px; border-radius: 50%; background: var(--ink); }
</style>
</head>
<body>
<div class="banner">
  <svg class="backdrop" viewBox="0 0 1200 306" aria-hidden="true">
    <defs>
      <linearGradient id="panelGlow" x1="0" y1="0" x2="0.3" y2="1">
        <stop offset="0" stop-color="#0a1a3d"/>
        <stop offset="0.45" stop-color="#12296b"/>
        <stop offset="1" stop-color="#1c47b0"/>
      </linearGradient>
    </defs>
    <rect width="1200" height="306" fill="#ffffff"/>
    <polygon points="0,0 882,0 847,306 0,306" fill="url(#panelGlow)"/>
  </svg>

  <svg class="photo" viewBox="0 0 1200 306" role="img" aria-label="Portrait photo of two smiling women, the business owners">
    <defs>
      <linearGradient id="photoTone" x1="0" y1="0" x2="1" y2="1">
        <stop offset="0" stop-color="#4a2f26"/>
        <stop offset="0.5" stop-color="#8a5a44"/>
        <stop offset="1" stop-color="#b07a5c"/>
      </linearGradient>
    </defs>
    <polygon points="896,0 1200,0 1200,306 862,306" fill="url(#photoTone)"/>
  </svg>

  <h1 class="headline">BOOMING ONLINE BUSINESS</h1>

  <svg class="ribbon" viewBox="0 0 770 48" aria-hidden="true">
    <polygon points="0,0 770,0 752,24 770,48 14,48 26,24" fill="#f6f21c"/>
  </svg>
  <p class="ribbon-text">Personal Development and Leadership Industry</p>

  <svg class="stars stars-left" viewBox="0 0 74 20" aria-hidden="true">
    <g fill="#f6f21c">
      <polygon points="10,1 12.4,7.2 19,7.5 13.8,11.6 15.6,18 10,14.3 4.4,18 6.2,11.6 1,7.5 7.6,7.2"/>
      <polygon transform="translate(27 0)" points="10,1 12.4,7.2 19,7.5 13.8,11.6 15.6,18 10,14.3 4.4,18 6.2,11.6 1,7.5 7.6,7.2"/>
      <polygon transform="translate(54 0)" points="10,1 12.4,7.2 19,7.5 13.8,11.6 15.6,18 10,14.3 4.4,18 6.2,11.6 1,7.5 7.6,7.2"/>
    </g>
  </svg>
  <p class="offer">MAKE UP TO $5,000 PER SALE</p>
  <svg class="stars stars-right" viewBox="0 0 74 20" aria-hidden="true">
    <g fill="#f6f21c">
      <polygon points="10,1 12.4,7.2 19,7.5 13.8,11.6 15.6,18 10,14.3 4.4,18 6.2,11.6 1,7.5 7.6,7.2"/>
      <polygon transform="translate(27 0)" points="10,1 12.4,7.2 19,7.5 13.8,11.6 15.6,18 10,14.3 4.4,18 6.2,11.6 1,7.5 7.6,7.2"/>
      <polygon transform="translate(54 0)" points="10,1 12.4,7.2 19,7.5 13.8,11.6 15.6,18 10,14.3 4.4,18 6.2,11.6 1,7.5 7.6,7.2"/>
    </g>
  </svg>

  <div class="benefits">
    <span>Simple 3 step system</span>
    <span class="dot"></span>
    <span>Make up to $5,000 per sale</span>
    <span class="dot"></span>
    <span>Not MLM</span>
  </div>
</div>
</body>
</html>
```